UX Design Document Management App Project

UPDATED PROJECT and INCREASED TOTAL COST. Also added a new design guideline document (4KR - Concept - The Lattice 170613.pdf).

We are a small start-up company based in Sydney, Australia. We have the ideas and coding skills to have built a revolutionary document management app that helps knowledge workers deal with information overload.

We are about to launch an alpha version of a document management app on the iPhone. We have created a series of screens but they lack the brilliance that only a talented graphic designer can deliver. So we would like to find a design partner who can make a contribution in two areas:

1. Make specific changes to our screens such as formatting images so they better blend into the background.
2. Examine our overall UX and either suggest changes or propose new design concepts.
3. Create a logo for this product.

We have completed a pretty comprehensive design brief that we attach to this project and also a set of our existing screen designs in a mix of Photoshop and Keynote formats that we can share with you.

Once we have launched are alpha product, we hope that the winner of this project (our future graphic design partner) will work with us on another project that aims to radically improve the UX of our app in time for a full version 1.0 launch later this year.

We'd like to lock-down the alpha UX in 5 to 10 days but if the ideas you have are exciting enough we can extend this time.

Project now has a SIGNIFICANTLY INCREASED BUDGET (almost doubled) and an expanded scope to deliver a logo for our product. Check out the additional design brief document just uploaded.

Hello Designers,

Just to let you know that we have updated the project and INCREASED THE TOTAL BUDGET. We have also added a new design guideline document (4KR - Concept - The Lattice 170613.pdf) to help inspire you!

The project now has a significantly increased budget (almost doubled) and an expanded scope to also deliver a logo for our Quillmark product. Check out the additional design brief document just uploaded.

Thanks for participating!

All the best,

Dalton

Barring any unforeseen circumstances, this design competition will remain open until midnight Pacific Standard Time this Sunday. That means about 10 am Sydney time this Monday, July 1st. Good luck and get your designs in!

Project Deadline Extended
Reason: I agreed to use PST not AEST!

Target Market(s)

individual knowledge workers: professionals, office workers/managers, university students, academics/researchers, etc.

Industry/Entity Type

Graphic Designer

Requirements
Must have
• professional, highly effective UX

```html
<!DOCTYPE html>
<html lang="en">
<head>
<meta charset="utf-8">
<title>Quillmark – onboarding screens</title>
<link rel="stylesheet" href="https://fonts.googleapis.com/css2?family=Didact+Gothic&display=swap">
<style>
  :root {
    --sheet: #d5d6d7;
    --teal: #0fa89a;
    --teal-soft: #a9dedd;
    --white: #ffffff;
    --ink: #111111;
    --text: #4a4a4a;
    --muted: #6e6e6e;
    --ring: #dcdcdc;
  }
  * { box-sizing: border-box; margin: 0; padding: 0; }
  html, body { width: 1200px; height: 1027px; overflow: hidden; }
  body {
    position: relative;
    background: var(--sheet);
    font-family: "Didact Gothic", "Helvetica Neue", Arial, sans-serif;
    color: var(--text);
  }
  .screen {
    position: absolute;
    width: 495px;
    height: 759px;
    background: linear-gradient(to bottom, var(--white) 45%, #f3f3f3 100%);
    overflow: hidden;
  }
  .screen--testimonial { left: 46px; top: 24px; }
  .screen--subscribe { left: 590px; top: 26px; }

  .app-bar {
    position: absolute; left: 0; top: 0; width: 100%; height: 84px;
    background: var(--teal);
  }
  .app-bar__title {
    position: absolute; left: 0; right: 0; top: 22px;
    text-align: center; color: var(--white); font-size: 31px; line-height: 40px;
  }
  .app-bar__icon { position: absolute; top: 18px; width: 50px; height: 50px; }
  .app-bar__icon--home { left: 18px; }
  .app-bar__icon--settings { right: 12px; }

  .hero {
    position: absolute; left: 0; top: 93px; width: 100%; height: 194px;
    background: linear-gradient(to bottom, #ebebeb 0%, #c9c9c9 55%, #6f6f6f 78%, #3c3c3c 100%);
  }

  .quote {
    position: absolute; left: 0; right: 0; top: 298px;
    text-align: center; font-size: 26px; line-height: 38px; color: var(--text);
  }

  .portrait {
    position: absolute; left: 10px; top: 406px; width: 228px; height: 228px;
    border-radius: 50%; border: 10px solid var(--ring);
    background: radial-gradient(circle at 50% 40%, #b8b8b8 0%, #8c8c8c 55%, #4a4a4a 100%);
  }
  .person { position: absolute; left: 283px; top: 482px; }
  .person__name { font-size: 24px; color: var(--ink); line-height: 28px; }
  .person__role { font-size: 12px; color: var(--muted); line-height: 14px; }

  .caption {
    position: absolute; left: 0; right: 0; top: 660px;
    text-align: center; font-size: 21px; color: var(--muted);
  }

  .pager { position: absolute; left: 164px; top: 712px; display: flex; gap: 14px; }
  .pager__dot { width: 22px; height: 22px; border-radius: 50%; background: var(--teal-soft); }
  .pager__dot--active { background: var(--teal); }

  .subscribe-button {
    position: absolute; left: 59px; top: 483px; width: 379px; height: 45px;
    background: var(--teal); color: var(--white);
    font-size: 24px; line-height: 45px; text-align: center;
  }
  .terms {
    position: absolute; left: 0; right: 0; top: 642px;
    text-align: center; font-size: 21px; line-height: 30px; color: var(--muted);
  }
  .terms__link { color: var(--teal); }

  .suggestions {
    position: absolute; left: 322px; top: 838px;
    font-size: 24px; line-height: 36.5px; color: var(--ink);
  }
  .suggestions__indent { padding-left: 14px; }
</style>
</head>
<body>

<section class="screen screen--testimonial">
  <header class="app-bar">
    <svg class="app-bar__icon app-bar__icon--home" viewBox="0 0 50 50" aria-label="Home">
      <circle cx="25" cy="25" r="22" fill="none" stroke="#fff" stroke-width="3"/>
      <path d="M13 25 L25 14 L37 25 L33.5 25 L33.5 35 L28 35 L28 29 L22 29 L22 35 L16.5 35 L16.5 25 Z" fill="#fff"/>
    </svg>
    <div class="app-bar__title">Quillmark</div>
    <svg class="app-bar__icon app-bar__icon--settings" viewBox="0 0 50 50" aria-label="Settings">
      <circle cx="25" cy="25" r="22" fill="none" stroke="#fff" stroke-width="3"/>
      <g fill="#fff" transform="translate(25 25)">
        <circle r="9"/>
        <rect x="-3" y="-14" width="6" height="6" rx="1"/>
        <rect x="-3" y="-14" width="6" height="6" rx="1" transform="rotate(45)"/>
        <rect x="-3" y="-14" width="6" height="6" rx="1" transform="rotate(90)"/>
        <rect x="-3" y="-14" width="6" height="6" rx="1" transform="rotate(135)"/>
        <rect x="-3" y="-14" width="6" height="6" rx="1" transform="rotate(180)"/>
        <rect x="-3" y="-14" width="6" height="6" rx="1" transform="rotate(225)"/>
        <rect x="-3" y="-14" width="6" height="6" rx="1" transform="rotate(270)"/>
        <rect x="-3" y="-14" width="6" height="6" rx="1" transform="rotate(315)"/>
      </g>
      <circle cx="25" cy="25" r="4" fill="var(--teal)"/>
    </svg>
  </header>
  <div class="hero" role="img" aria-label="Black and white photo of a cable-stayed bridge over a valley"></div>
  <p class="quote">“ I’ve lost count of times my deadline<br>has been saved by Quillmark Summeries ”</p>
  <div class="portrait" role="img" aria-label="Portrait photo of the reviewer"></div>
  <div class="person">
    <div class="person__name">Sample Name</div>
    <div class="person__role">Analyst in Sample Company</div>
  </div>
  <p class="caption">Quillmark Summeries are fast and accurate</p>
  <div class="pager">
    <span class="pager__dot"></span>
    <span class="pager__dot pager__dot--active"></span>
    <span class="pager__dot"></span>
    <span class="pager__dot"></span>
    <span class="pager__dot"></span>
  </div>
</section>

<section class="screen screen--subscribe">
  <header class="app-bar">
    <svg class="app-bar__icon app-bar__icon--home" viewBox="0 0 50 50" aria-label="Home">
      <circle cx="25" cy="25" r="22" fill="none" stroke="#fff" stroke-width="3"/>
      <path d="M13 25 L25 14 L37 25 L33.5 25 L33.5 35 L28 35 L28 29 L22 29 L22 35 L16.5 35 L16.5 25 Z" fill="#fff"/>
    </svg>
    <div class="app-bar__title">Quillmark</div>
    <svg class="app-bar__icon app-bar__icon--settings" viewBox="0 0 50 50" aria-label="Settings">
      <circle cx="25" cy="25" r="22" fill="none" stroke="#fff" stroke-width="3"/>
      <g fill="#fff" transform="translate(25 25)">
        <circle r="9"/>
        <rect x="-3" y="-14" width="6" height="6" rx="1"/>
        <rect x="-3" y="-14" width="6" height="6" rx="1" transform="rotate(45)"/>
        <rect x="-3" y="-14" width="6" height="6" rx="1" transform="rotate(90)"/>
        <rect x="-3" y="-14" width="6" height="6" rx="1" transform="rotate(135)"/>
        <rect x="-3" y="-14" width="6" height="6" rx="1" transform="rotate(180)"/>
        <rect x="-3" y="-14" width="6" height="6" rx="1" transform="rotate(225)"/>
        <rect x="-3" y="-14" width="6" height="6" rx="1" transform="rotate(270)"/>
        <rect x="-3" y="-14" width="6" height="6" rx="1" transform="rotate(315)"/>
      </g>
      <circle cx="25" cy="25" r="4" fill="var(--teal)"/>
    </svg>
  </header>
  <div class="hero" role="img" aria-label="Black and white photo of a cable-stayed bridge over a valley"></div>
  <p class="quote">“ Hurry ! your future success is just<br>a single tap away&nbsp; ”</p>
  <div class="subscribe-button">Subscribe Now&nbsp; ($29.90 p/a)</div>
  <p class="terms">By Subscription you agree to our<br><span class="terms__link">Terms &amp; Conditions</span></p>
  <div class="pager">
    <span class="pager__dot"></span>
    <span class="pager__dot"></span>
    <span class="pager__dot"></span>
    <span class="pager__dot pager__dot--active"></span>
    <span class="pager__dot"></span>
  </div>
</section>

<div class="suggestions">
  <p>Suggestions;</p>
  <p>1. Decrease the amount of text in these screens</p>
  <p>2. Use the upper bar (without icons if needed)</p>
  <p class="suggestions__indent">from the beginning of the app</p>
</div>

</body>
</html>
```